Willowmere Family Program (special education services) needs a Brochure Design

We need a brochure design for a new company. We are an Willowmere Family Program providing special education, speech, occupational and physical therapy to children birth - 3 years of age. The children we provide services for have a wide range of disabilities. Please include some stock photos if possible. Brochure text is attached.
Updates

Project Deadline Extended Reason: 1. We would like to see pictures that are multicultural (not all Caucasian).2. Some of the pictures (which were taken from our website) that were used by designers are of children that are older than 3 yrs. Please use new/different pictures of children birth-3 yrs. 3. Update the text that is in the brochure. Original line is: "The Willowmere Family Program (WFP) is a statewide public program for infants and toddlers with special needs". Replace with "The Willowmere Family Program (WFP) is a statewide public program for infants and toddlers, ages birth to 3 years, with special needs". Added Monday, February 6, 2017

Target Market(s)

Parents, Doctors, Daycare Providers

Industry/Entity Type

Education

Font styles to use
Serif
Sans Serif

Requirements
Must have
• A balance between professional looking, while child friendly and colorful
Nice to have
• A few stock pictures of children (birth-age 3)

```html
<!DOCTYPE html>
<html lang="en">
<head>
<meta charset="utf-8">
<title>Willowmere Family Program Brochure</title>
<link href="https://fonts.googleapis.com/css2?family=Bitter:wght@400;700&family=Open+Sans:wght@400;600;700&display=swap" rel="stylesheet">
<style>
:root{
  --green:#7cae2a;
  --green-light:#9cc43a;
  --yellow:#f7ec1c;
  --gold:#f5d31a;
  --orange:#ea5a1d;
  --orange-box:#e9541f;
  --red:#d9262f;
  --blue:#2a9ad6;
  --ink:#2b2b2b;
  --body:#3d3d3d;
  --white:#ffffff;
  --page:#ebe8e3;
}
*{margin:0;padding:0;box-sizing:border-box}
html,body{width:960px;height:1200px;overflow:hidden;background:var(--page)}
body{position:relative;font-family:"Open Sans",sans-serif;color:var(--body)}
.spread{position:absolute;left:115px;width:730px;height:516px;background:var(--white);overflow:hidden;box-shadow:0 4px 14px rgba(0,0,0,.18)}
.spread--outside{top:50px}
.spread--inside{top:630px}
.spread svg.art{position:absolute;left:0;top:0;width:730px;height:516px}
.block{position:absolute}
p{font-size:7px;line-height:1.62;text-align:justify}
p + p{margin-top:7px}

/* outside spread */
.welcome{left:20px;top:196px;width:194px;text-align:right;font-family:"Bitter",serif;font-weight:700;line-height:1.15}
.welcome .lead{color:var(--white);font-size:13px;display:block;margin-bottom:2px}
.welcome .name{color:var(--yellow);font-size:17px;display:block}
.welcome-copy{left:19px;top:282px;width:197px}
.welcome-copy p{color:var(--white)}
.welcome-copy strong{font-weight:700}

.referrals{left:258px;top:58px;width:218px}
.section-title{font-family:"Bitter",serif;font-weight:700;font-size:14px;color:var(--red);margin-bottom:6px}
.referrals .numbers{font-size:7px;line-height:1.6;color:var(--ink);margin-top:10px}
.referrals .numbers b{font-weight:700}
.contact-box{left:267px;top:360px;width:196px;height:68px;background:var(--orange-box);border-radius:5px;color:var(--white);text-align:center;font-family:"Bitter",serif;font-weight:700;padding-top:9px}
.contact-box .phone{font-size:13px;color:var(--gold);display:block;margin-bottom:3px}
.contact-box .line{font-size:9.5px;display:block;line-height:1.75}
.office{left:262px;top:451px;width:208px;text-align:center;font-family:"Bitter",serif;font-weight:700;font-size:10px;line-height:1.45;color:var(--ink)}

.brand{left:498px;top:90px;width:222px;text-align:center}
.brand-mark{width:22px;height:22px;border-radius:50%;background:var(--orange);margin:0 auto 10px}
.brand-name{font-family:"Bitter",serif;font-weight:400;font-size:13.5px;line-height:1.35;color:var(--ink);font-variant:small-caps;letter-spacing:.3px}
.cover-tag{left:508px;top:412px;width:206px;text-align:right;font-family:"Bitter",serif;font-weight:700;font-size:11px;line-height:1.6;color:var(--white)}
.cover-tag em{font-style:normal;color:var(--gold)}

/* inside spread */
.services{left:23px;top:36px;width:210px}
.services .section-title{font-size:14px;margin-bottom:10px}
.list{list-style:none;margin-bottom:16px}
.list li{font-size:10px;font-weight:600;color:var(--ink);line-height:1.85;padding-left:11px;position:relative}
.list li::before{content:"";position:absolute;left:1px;top:7px;width:4px;height:4px;border-radius:50%;background:var(--ink)}
.section-title--green{color:var(--green)}
.mission{left:270px;top:290px;width:198px}
.mission .section-title{font-size:12.5px;margin-bottom:5px}
.family{left:502px;top:212px;width:218px}
.family h3{font-family:"Bitter",serif;font-weight:700;font-size:10.5px;line-height:1.45;margin-bottom:5px;max-width:182px}
.family h3.g{color:var(--green)}
.family h3.r{color:var(--red)}
.family p{text-align:left;margin-bottom:14px}
</style>
</head>
<body>

<section class="spread spread--outside" aria-label="Brochure outside">
  <svg class="art" viewBox="0 0 730 516">
    <defs>
      <linearGradient id="gPlay" x1="0" y1="0" x2="1" y2="1">
        <stop offset="0" stop-color="#e7d6c4"/><stop offset=".5" stop-color="#c99b7d"/><stop offset="1" stop-color="#6f9bd1"/>
      </linearGradient>
      <linearGradient id="gToddler" x1="0" y1="0" x2="0" y2="1">
        <stop offset="0" stop-color="#e9c9a3"/><stop offset="1" stop-color="#b56f3d"/>
      </linearGradient>
      <linearGradient id="gSnack" x1="0" y1="0" x2="1" y2="0">
        <stop offset="0" stop-color="#f3dc55"/><stop offset=".45" stop-color="#4d7bc6"/><stop offset="1" stop-color="#e14b3a"/>
      </linearGradient>
    </defs>
    <path d="M0 0H243V132Q120 150 0 196Z" fill="url(#gPlay)" role="img" aria-label="Photo of a caregiver with three toddlers playing at a table"/>
    <path d="M0 200Q120 152 243 138V516H0Z" fill="var(--green)"/>
    <path d="M0 196Q120 150 243 132V138Q120 152 0 200Z" fill="var(--white)"/>
    <circle cx="52" cy="166" r="52" fill="var(--orange)"/>
    <circle cx="52" cy="166" r="47" fill="var(--white)"/>
    <circle cx="52" cy="166" r="44" fill="url(#gToddler)" role="img" aria-label="Photo of a toddler sitting with stacking blocks"/>
    <path d="M290 0H486V172Q440 60 290 0Z" fill="var(--yellow)"/>
    <path d="M486 170Q560 150 640 190Q690 150 730 160V176Q660 170 610 196Q560 166 486 178Z" fill="var(--blue)"/>
    <path d="M600 196Q670 160 730 164V188Q670 182 600 196Z" fill="var(--green-light)"/>
    <path d="M486 180Q560 168 610 198Q670 186 730 190V368Q620 372 486 424Z" fill="url(#gSnack)" role="img" aria-label="Photo of two toddlers eating a snack at a table"/>
    <path d="M486 424Q620 372 730 368V380Q610 386 486 436Z" fill="var(--orange)"/>
    <path d="M486 436Q610 386 730 380V516H486Z" fill="var(--red)"/>
  </svg>

  <h2 class="block welcome"><span class="lead">Welcome to the</span><span class="name">Willowmere Family Program</span></h2>
  <div class="block welcome-copy">
    <p>The Willowmere Family Program (WFP) is a statewide public program for infants and toddlers, ages birth to 3 years, with special needs. The Program provides many different types of early intervention services to infant and toddlers with disabilities and their families. Children with diagnosed conditions that lead to developmental delays (such as Down syndrome, cerebral palsy, autism, etc.) are eligible for the WFP. Children with no diagnosis who have delays in development may be eligible for the WFP if their delays are serious enough. In the State, the Department of Health is the lead state agency responsible for the Willowmere Family Program.</p>
    <p>The early years of a child's life are very important. During the infant and toddler years, children grow quickly and have so much to learn. Some children and families face special challenges and need extra help. <strong>EARLY HELP DOES MAKE A DIFFERENCE!</strong></p>
  </div>

  <div class="block referrals">
    <h2 class="section-title">Referrals</h2>
    <p>If you have concerns about your child's development, you can call your county's Willowmere Family Program to refer your child (please see your county's number listed below). The Center for Young Children can help you make the referral to the Willowmere Family Program if you wish. If your child is found to be eligible for services by someone approved to perform this evaluation, you, county staff, and other team members will make a plan to help your child – and your family.</p>
    <p>Early intervention services in your plan and authorized by the county are provided at no cost to you. The county will arrange for the services to be provided and will choose the provider based on the needs of your child and family. Your child's health insurance may be used to cover some of the costs. All other costs for WFP services are paid for by your county and the State.</p>
    <p>Early intervention services are provided where it's best for the child – in places such as your home, daycare, or other community settings. The WFP covers the cost of early intervention services only. The WFP does not pay for day care or other fees charged by community settings.</p>
    <div class="numbers"><b>Referrals:</b><br>North County: (555) 310-4420<br>South County: (555) 310-4421 / City: (555) 310-4422</div>
  </div>

  <div class="block contact-box">
    <span class="phone">Phone: (555) 240-7310</span>
    <span class="line">Fax: (555) 240-7311</span>
    <span class="line">www.harborviewkids.org</span>
  </div>
  <div class="block office">Administrative Office:<br>72 Linden Avenue<br>Maple Falls, ST 00000</div>

  <div class="block brand">
    <div class="brand-mark"></div>
    <div class="brand-name">Harborview Center for<br>Young Children</div>
  </div>
  <div class="block cover-tag"><em>The Willowmere Family Program (WFP)</em> is a statewide public program for infants and toddlers, ages birth to 3 years, with special needs.</div>
</section>

<section class="spread spread--inside" aria-label="Brochure inside">
  <svg class="art" viewBox="0 0 730 516">
    <defs>
      <radialGradient id="gBaby" cx=".5" cy=".45" r=".55">
        <stop offset="0" stop-color="#f4e2d3"/><stop offset=".6" stop-color="#f7f1ec"/><stop offset="1" stop-color="#ffffff"/>
      </radialGradient>
      <linearGradient id="gGirls" x1="0" y1="0" x2="1" y2="0">
        <stop offset="0" stop-color="#d94a3a"/><stop offset=".5" stop-color="#e8c29e"/><stop offset="1" stop-color="#8c6bb5"/>
      </linearGradient>
      <linearGradient id="gBoard" x1="0" y1="0" x2="1" y2="1">
        <stop offset="0" stop-color="#9fc6e8"/><stop offset=".6" stop-color="#3f8fd0"/><stop offset="1" stop-color="#e24a36"/>
      </linearGradient>
    </defs>
    <path d="M0 0H486V212Q440 30 0 16Z" fill="var(--orange)"/>
    <rect x="232" y="60" width="252" height="216" fill="url(#gBaby)" role="img" aria-label="Photo of a smiling baby sitting with colourful stacking cups"/>
    <path d="M0 360Q140 346 225 362V368Q140 354 0 368Z" fill="var(--red)"/>
    <path d="M0 372Q140 356 243 370V516H0Z" fill="url(#gGirls)" role="img" aria-label="Photo of three smiling toddler girls lying on a play mat"/>
    <rect x="486" y="0" width="244" height="200" fill="var(--green-light)"/>
    <path d="M486 160Q540 70 730 36V216Q620 166 486 172Z" fill="url(#gBoard)" role="img" aria-label="Photo of a toddler boy playing with a numbered activity board"/>
    <path d="M486 172Q620 166 730 216V224Q620 176 486 186Z" fill="var(--red)"/>
    <path d="M486 186Q620 176 730 224V516H486Z" fill="var(--white)"/>
  </svg>

  <div class="block services">
    <h2 class="section-title">Services Provided</h2>
    <ul class="list">
      <li>ABA (Applied Behavior Analysis)</li>
      <li>Special Education/Instruction</li>
      <li>Speech Therapy</li>
      <li>Occupational Therapy</li>
      <li>Physical Therapy</li>
      <li>Family Training</li>
      <li>Social Work</li>
    </ul>
    <h2 class="section-title section-title--green">Evaluations Conducted</h2>
    <ul class="list">
      <li>Developmental / Cognitive</li>
      <li>Psychological</li>
      <li>Speech Therapy</li>
      <li>Occupational Therapy</li>
      <li>Physical Therapy</li>
      <li>Feeding Therapy</li>
    </ul>
  </div>

  <div class="block mission">
    <h2 class="section-title">Mission Statement</h2>
    <p>The Center for Young Children believes that all children have the ability to learn and have the right to a quality education. We are committed to providing individualized and developmentally appropriate educational and therapeutic services that are based upon a child's strengths and needs and that address all areas of development. These services are designed to enhance the capacities of families to meet their child's developmental needs and work to ensure that children reach their full potential.</p>
    <p>The Center promotes a family centered and holistic approach in which the families perspective, values and culture is respected and one in which the parents and caregivers play an integral part in their child's overall education.</p>
  </div>

  <div class="block family">
    <h3 class="g">Early Intervention services can help you and your family:</h3>
    <p>Learn the best ways to care for your child. Support and promote your child's development. Include your child in your family and community life.</p>
    <h3 class="r">Early Intervention services can be provided anywhere in the community, including:</h3>
    <p>Your home, child care center or family day care home, recreational centers, play groups, playgrounds, libraries, or any place parents and children go for fun and support. In addition, services are provided at early childhood programs and early intervention facilities and centers.</p>
    <h3 class="r">As a parent, you help decide:</h3>
    <p>What early intervention services your child and family need; The outcomes of early intervention that are important for your child and family; When and where your child and family will get early intervention services; Who will provide services to your child and family.</p>
  </div>
</section>

</body>
</html>
```